New KVT Identification sticker

Looking for a new look to the attached sticker. We want to keep the original in the design and would like to incorporate our vision statement and company history some way into the new design. Holograph overlay would be encouraged in the sticker design, You can also research more about the company through the website: http://www.lumbrade.example/
Updates

Please remember in the designs you do not have to capture the all the verbiage within the mission or vision statement or the history. I want you to take the verbiage meaning or highlight the history within the design. Also the old design must be somewhere within the new design to keep the history. I do like some of what is being done but I do not see the story within the design as of yet. A few more things about the company: High quality Union Proud shop Employing hard working people Craftsmanship Years of service in the industry Hard work and dedication goes into every blade overhaul Go to the kestrel vane technical website and learn more about the company. It will be the message in the design and the feeling proud of the work that was done message that I think the CEO will be looking for. Keep it simple but bring make it modern. I know we can not capture everything in one sticker. But use something that will help draw people into the overhaul message that the work completed by KVT is the highest quality and it was done to the highest standard by experienced people that care about what they do. OK Thanks

Thank you everyone that has been submitting your designs. So many great ideals. Sorry I have not been getting back to everyone. I am reviewing all the designs and waiting for some feed back from the others involved in this project. It is going to take at least this week to get through the designs and to narrow down the selection. Because this is a group effort on my side it is not easy to get everyone together to get a fast decision so I apologies in advance for the length of time this is taking. I hope to be working with some of you soon to tweak the designs and for our group to pick the design we will be going with. Please be patient and we will be in touch soon. This is the first time we have used this service so we are learning as we go forward. Thank you again, I look forward to working with one of you soon. You all have been great. Be back to you all soon with more information as I get it.

Target Market(s)

Aircraft operators that fly aircraft with propellers

Colors

Designer to choose colors to be used in the design.

Requirements
Must have
• Incorporate our old design into the new one
Nice to have
• Hologram

```html
<!DOCTYPE html>
<html lang="en">
<head>
<meta charset="utf-8">
<title>KVT Identification Sticker</title>
<link rel="stylesheet" href="https://fonts.googleapis.com/css2?family=Archivo+Black&family=Oswald:wght@600;700&display=swap">
<style>
  :root {
    --page: #fdfdfd;
    --panel: #484342;
    --violet: #a800ff;
    --orchid: #c95fcf;
    --peach: #e8a98f;
    --lemon: #fff06a;
    --lime: #c8f57a;
    --mint: #8ff59c;
    --sky: #7593ff;
    --iris: #8b4dff;
  }
  * { margin: 0; padding: 0; box-sizing: border-box; }
  html, body {
    width: 1060px; height: 1200px; overflow: hidden;
    background: var(--page);
  }
  .canvas { position: relative; width: 1060px; height: 1200px; }

  .sticker {
    position: absolute; left: 272px; top: 200px;
    width: 516px; height: 798px; border-radius: 38px; overflow: hidden;
    background: linear-gradient(180deg,
      var(--sky) 6%, var(--iris) 28%, var(--violet) 40%,
      var(--orchid) 55%, var(--peach) 66%, var(--lemon) 80%,
      var(--lime) 90%, var(--mint) 100%);
  }
  .sticker__band {
    position: absolute; left: 25px; right: 25px; height: 25px;
    background: repeating-linear-gradient(90deg,
      var(--mint) 0 27px, var(--sky) 27px 54px, var(--lime) 54px 81px,
      var(--iris) 81px 108px, var(--lemon) 108px 135px, var(--violet) 135px 162px);
  }
  .sticker__band--top { top: 0; }
  .sticker__band--bottom { bottom: 0; }

  .panel {
    position: absolute; left: 25px; top: 25px;
    width: 465px; height: 749px; border-radius: 16px;
    background: var(--panel);
  }

  .brand-mark {
    position: absolute; left: 0; right: 0; top: 95px;
    display: flex; align-items: center; justify-content: center; gap: 18px;
  }
  .brand-mark__square { width: 40px; height: 40px; background: var(--violet); }
  .brand-mark__name {
    font-family: "Oswald", sans-serif; font-weight: 700;
    font-size: 120px; line-height: 1; color: var(--lemon); letter-spacing: 4px;
  }

  .small-line {
    position: absolute; left: 0; right: 0; text-align: center;
    font-family: "Oswald", sans-serif; font-weight: 600; text-transform: uppercase;
  }
  .tagline {
    top: 351px; font-size: 15.5px; letter-spacing: 0.3px;
    background: linear-gradient(90deg, var(--orchid), var(--peach));
    -webkit-background-clip: text; background-clip: text; color: transparent;
  }
  .services { top: 635px; font-size: 15.5px; line-height: 25px; color: var(--lemon); letter-spacing: 0.2px; }
  .since {
    top: 703px; font-size: 23px; letter-spacing: 0.5px;
    background: linear-gradient(90deg, var(--iris), var(--lime));
    -webkit-background-clip: text; background-clip: text; color: transparent;
  }

  .company-name { position: absolute; left: 0; top: 0; width: 465px; height: 749px; }
  .company-name text { font-family: "Archivo Black", sans-serif; fill: var(--orchid); }
</style>
</head>
<body>
<div class="canvas">
  <div class="sticker">
    <div class="sticker__band sticker__band--top"></div>
    <div class="sticker__band sticker__band--bottom"></div>

    <div class="panel">
      <div class="brand-mark">
        <span class="brand-mark__square"></span>
        <span class="brand-mark__name">KVT</span>
      </div>

      <p class="small-line tagline">Provide aviation professionals the finest quality</p>

      <svg class="company-name" viewBox="0 0 465 749" aria-label="Kestrel Vane">
        <text x="33" y="490" font-size="132" textLength="400" lengthAdjust="spacingAndGlyphs">KESTREL</text>
        <text x="33" y="573" font-size="92" textLength="400" lengthAdjust="spacingAndGlyphs">VANE</text>
      </svg>

      <p class="small-line services">Inspection, repair and overhauls of regional<br>aircraft propellers and large propeller systems</p>
      <p class="small-line since">Since 1946</p>
    </div>
  </div>
</div>
</body>
</html>
```